lockenbrise gemeinnütziges Projekt A4 Falzflyer
Zielgruppe
Wir Sammeln und verarbeiten Haarspenden zu Perücken für Krebskranke Menschen.
Mit dem Flyer möchten wir Friseure aus ganz Deutschland gewinnen sich sowohl als Haarspendensammelstelle als auch eine Art Beratungsstelle und für die Frisurengestalltung der Perücken für die betroffenen zu engagieren.
Was passiert mit den Haaren:
1. Wir sammeln die Haarspenden bei uns (wir erhalten diese Gesammelt von Friseuren und direkt von Einzelspendern )
2. Wir dokumentieren, Katalogisieren jeden einzelnen Zopf und stellen Ihn online.
3. Betroffene können sich online http://lockenbrise.com/ aus der Haarspenden eine Perücke zusammen stellen //// bzw. wir werden einige Perücken aus gespendeten Haaren vorproduzieren.
4. Es entstehen nur die Kosten der Perückenproduktion welche von der Krankenkasse bzw. vom Betroffenen getragen werden. Die gespendeten Haare werden als Spende weitergegeben.
5. Die Frisurengastallung und Beratung, soll vom Friseurpartner statt finden.
Aufgabenstellung
Ich finde selbst der Flyer hat Momentan ein wenig viel Text und braucht eine komplett neue Struktur.
Bitte, bitte zaubert einen ansprechenden unersichtlichen Falz-flyer.
Das Design soll klar und schlicht sein Ihr könnt euch am CI der Webseite halten. http://lockenbrise.com/
Bitte beachtet für den Inhalt die datei: "An die Zweithaarstudios_PublikationSept2017"
Format A4 Falzflyer 4 seiten
Bilder von einer sammelaktion
https://www.dateiablage-beispiel.de/sh/q3mxk8w2r47b5tz/KLPWR82vnTqzXcha-m4HEBkvo?dl=0

```html
<!DOCTYPE html>
<html lang="de">
<head>
<meta charset="utf-8">
<title>Lockenbrise – Partner werden</title>
<link href="https://fonts.googleapis.com/css2?family=Quicksand:wght@400;500;600;700&display=swap" rel="stylesheet">
<style>
  :root {
    --teal: #6a9eab;
    --teal-dark: #5b8f9c;
    --text: #4a4a4a;
    --text-strong: #3d3d3d;
    --ink: #111111;
    --backdrop: #bdbdbd;
    --paper: #ffffff;
  }
  * { margin: 0; padding: 0; box-sizing: border-box; }
  html, body {
    width: 1200px; height: 1196px; overflow: hidden;
    background: var(--backdrop);
    font-family: "Quicksand", sans-serif;
    color: var(--text);
  }
  .flyer-page {
    position: absolute; left: 203px; top: 17px;
    width: 818px; height: 1157px;
    background: var(--paper);
    box-shadow: 4px 6px 10px rgba(0,0,0,0.35);
  }
  .flyer-page > * { position: absolute; }
  .section-title { left: 60px; top: 42px; font-size: 21px; font-weight: 500; color: #5a5a5a; }
  .section-band {
    left: 0; top: 78px; width: 100%; height: 30px;
    background: var(--teal); color: #fff;
    font-size: 15.5px; font-weight: 600; line-height: 30px; padding-left: 60px;
  }
  .headline { left: 60px; top: 133px; font-size: 21.5px; font-weight: 600; color: var(--teal); }
  .intro {
    left: 60px; top: 184px; width: 470px;
    font-size: 15.5px; line-height: 22px; font-weight: 600; color: var(--text-strong);
  }
  .bullet {
    left: 60px; width: 480px; font-size: 15.5px; line-height: 22px;
    padding-left: 10px; text-indent: -10px;
  }
  .bullet-salons { top: 240px; font-weight: 500; }
  .bullet-info { top: 398px; font-weight: 600; color: var(--text-strong); }
  .detail { left: 70px; top: 480px; width: 470px; font-size: 15.5px; line-height: 22px; font-weight: 500; }
  .photo { left: 566px; width: 207px; height: 134px; }
  .photo-haircut { top: 230px; background: linear-gradient(120deg, #5a3b2c 0%, #8a6048 40%, #c9d2c0 70%, #e8e6e2 100%); }
  .photo-sign { top: 470px; background: linear-gradient(135deg, #e4e4e4 0%, #f6f6f6 40%, #d8d8d8 100%); }
  .call-to-action {
    left: 71px; top: 661px; font-size: 21.5px; line-height: 32px; font-weight: 600; color: var(--teal);
  }
  .greeting { left: 71px; top: 788px; font-size: 21.5px; font-weight: 600; color: var(--teal); }
  .brand-name {
    left: 331px; top: 918px; width: 200px; text-align: center;
    font-size: 29px; font-weight: 500; color: var(--teal-dark); letter-spacing: 0.5px;
  }
  .contact { left: 336px; top: 983px; font-size: 15.5px; line-height: 18px; color: var(--ink); font-weight: 500; }
  .contact p + p { margin-top: 8px; }
  .footer-band { left: 0; top: 1145px; width: 100%; height: 12px; background: var(--teal); }
</style>
</head>
<body>
  <main class="flyer-page">
    <h2 class="section-title">So können Sie mithelfen</h2>
    <div class="section-band">Bewerben Sie sich als Partner</div>
    <h1 class="headline">Jede Haarspende macht einen anderen Menschen glücklicher</h1>

    <p class="intro">Als Partner des Haarspende-Projektes, arbeiten Sie mit uns zusammen. Das bedeutet:</p>

    <p class="bullet bullet-salons">• Wir vermitteln die Empfänger/innen der Haarspenden an Salons, die durch das Haarspende-Projekt zertifiziert wurden, damit sie in ihrem Salon abschließende Beratungen bekommen und damit die Perücken aus den gespendeten Haaren übergeben und eingeschnitten werden können.</p>

    <div class="photo photo-haircut" role="img" aria-label="Foto: Friseur schneidet langes braunes Haar mit Schere und Kamm"></div>

    <p class="bullet bullet-info">• In Zusammenarbeit mit Ihnen informieren wir in ihrem Salon über das Projekt, damit die Menschen in ihrer Umgebung erfahren, dass sie sich an Sie wenden können.</p>

    <p class="detail">Kunden und Kundinnen, die bei Ihnen ihre Haare spenden möchten, werden durch ein Hinweisschild mit dem Projekt aufmerksam gemacht.<br>Wir stellen Ihnen Versandtaschen für diese Kundinnen zur Verfügung, die sich im Zusammenhang mit ihrer Spende bei Ihnen die Haare schneiden lassen möchten.</p>

    <div class="photo photo-sign" role="img" aria-label="Foto: Hinweisschild für zertifizierte Partnersalons an einer Glasscheibe"></div>

    <p class="call-to-action">Möchten Sie Partner des Projektes „Lockenbrise“ werden?<br>Rufen Sie uns gerne an unter: 0781 - 12 345 670<br>Wir freuen uns auf die Kooperation mit Ihnen!</p>

    <p class="greeting">Mit herzlichen Grüßen</p>

    <div class="brand-name">lockenbrise</div>

    <address class="contact" style="font-style: normal;">
      <p>Am Birkenhang 5<br>77654 Musterstadt</p>
      <p>info@lockenbrise.com<br>www.lockenbrise.com</p>
      <p>TEL: 0781 - 12 345 670</p>
    </address>

    <div class="footer-band"></div>
  </main>
</body>
</html>
```